Menu Design Project

This project is for a carry-out food menu, which will also be mailed to approximately 10K customers in the surrounding 2-3 mile area. Fried chicke...

Target Market(s)

Menus will be provided to existing customers at store for call-in orders, but also will be mailed to businesses/residents within 2-3 mile radius. We are surrounded by industrial parks, and our typical customers are nearby workers.

Industry/Entity Type

Fast Food Restaurant

Requirements
Must have
• Would like a menu that features high quality photos of the food items, in addition to descriptive details. For instance "Our chicken is cooked to perfection using our own blend of seasonings".
Nice to have
• We would like to see the new logo on the cover, displayed with creative, eye-catching colors and/or designs. The menu will most likely be easiest to read when set among a lighter colored background. We would like for food to be displayed using vivid colors, with a photo technique that gives the appearance of sizzling hot, yet moist and tasty.
Should not have
• Prefer a font that is easy to read, with a clear, uncluttered layout

```html
<!DOCTYPE html>
<html lang="en">
<head>
<meta charset="utf-8">
<title>The Crispy Coop – Menu</title>
<link href="https://fonts.googleapis.com/css2?family=Montserrat:wght@500;700;800;900&family=Lobster&family=Open+Sans:wght@400;600;700&display=swap" rel="stylesheet">
<style>
:root{
  --red:#d8282a;
  --red-dark:#a9161a;
  --yellow:#fbe820;
  --orange:#f07b20;
  --ink:#1d1d1d;
  --cream:#fdf5d6;
  --slate:#2b2b2b;
  --white:#ffffff;
}
*{box-sizing:border-box;margin:0;padding:0}
html,body{width:1200px;height:1000px;overflow:hidden;background:#fff}
body{position:relative;font-family:"Montserrat",sans-serif;color:var(--ink)}
.sheet{position:absolute;top:148px;height:704px;width:543px;overflow:hidden}
.sheet--outside{left:42px}
.sheet--inside{left:614px;background:var(--cream)}

/* ---------- cover ---------- */
.cover{position:absolute;left:0;top:0;width:543px;height:235px}
.cover__flank{position:absolute;top:0;height:235px;background:radial-gradient(circle at 70% 30%,#ef3b3b,var(--red) 45%,var(--red-dark))}
.cover__flank--left{left:0;width:166px}
.cover__flank--right{left:376px;width:167px}
.cover__center{position:absolute;left:166px;top:0;width:210px;height:235px;background:var(--yellow);overflow:hidden}
.cover__rot{position:absolute;width:235px;height:210px;left:-12.5px;top:12.5px;transform:rotate(90deg);display:flex;flex-direction:column;align-items:center;padding-top:14px}
.cover__address{font-family:"Open Sans",sans-serif;font-size:8px;color:var(--ink)}
.cover__phone{font-size:19px;font-weight:800;color:var(--red);margin-top:2px}
.cover__tagline{font-family:"Lobster",sans-serif;font-size:15px;color:var(--orange);margin-top:2px}
.cover__name{font-family:"Lobster",sans-serif;font-size:30px;color:var(--red);margin-top:22px}

/* ---------- party platters ---------- */
.platters{position:absolute;left:0;top:235px;width:543px;height:237px;background:linear-gradient(90deg,#1f1f1f,#3a3a3a 50%,#202020)}
.platters__rot{position:absolute;width:237px;height:543px;left:153px;top:-153px;transform:rotate(-90deg);display:flex;flex-direction:column;align-items:center;text-align:center}
.platters__head{margin-top:16px;line-height:.95}
.platters__title{font-family:"Montserrat",sans-serif;font-weight:900;font-size:33px;color:var(--yellow);letter-spacing:1px}
.platters__title span{color:var(--red)}
.platters__sub{font-family:"Lobster",sans-serif;font-size:22px;color:var(--white);margin-top:4px}
.platters__lead{margin-top:20px;font-size:9.5px;font-weight:700;color:var(--yellow);line-height:1.3;width:170px}
.platters__body{font-family:"Open Sans",sans-serif;font-size:6.8px;color:#e8e8e8;line-height:1.45;width:180px;margin-top:6px}
.platters__photo{margin-top:14px;width:237px;height:220px;background:radial-gradient(circle at 40% 55%,#c9692a,#8a3b1c 45%,#4a2a1e 80%)}
.platters__cta{margin-top:14px;font-size:9px;font-weight:800;color:var(--yellow);line-height:1.35}
.platters__cta b{font-size:12px;font-weight:900}
.platters__phone{font-size:21px;font-weight:900;color:var(--white);margin-top:2px}

/* ---------- menu blocks ---------- */
.menu-title{text-align:center;font-weight:900;font-size:19px;letter-spacing:.5px;color:var(--slate)}
.menu-title .hot{color:var(--red)}
.menu-title .star{font-size:14px;color:var(--slate);margin:0 8px;vertical-align:2px}
.menu-cols{display:grid;grid-template-columns:172px 172px 172px;column-gap:14px}
.col-head{font-family:"Lobster",sans-serif;color:var(--red);font-size:15px;text-align:center;border-bottom:2px solid var(--slate);padding-bottom:1px;margin-bottom:8px}
.items{list-style:none;font-size:10px;font-weight:700;line-height:15.5px;padding-left:10px}
.items .red{color:var(--red)}
.items .note{display:block;font-family:"Open Sans",sans-serif;font-style:italic;font-weight:400;font-size:8px;line-height:10px;margin-bottom:3px}
.items .script{font-family:"Lobster",sans-serif;font-weight:400;color:var(--orange);font-size:11px;margin-left:4px}
.size-note{font-family:"Lobster",sans-serif;color:var(--orange);font-size:12.5px;padding-left:10px;margin-bottom:2px}
.boxed{border:2px solid var(--orange);margin:10px 10px 0 8px;padding:4px 8px 4px 8px;list-style:none;font-size:10px;font-weight:700;line-height:13.5px}
.boxed .red{color:var(--red)}

/* breakfast (printed upside down for the fold) */
.breakfast{position:absolute;left:0;top:472px;width:543px;height:232px;background:var(--cream);transform:rotate(180deg);padding-top:10px}
.breakfast .menu-title{font-size:18px;margin-bottom:5px}
.breakfast .menu-title small{font-size:9px;font-weight:700;margin-left:8px}
.breakfast .items{line-height:14px;font-size:9.5px}
.breakfast .menu-cols{grid-template-columns:170px 170px 171px;column-gap:16px}
.split{display:flex;gap:6px}
.split .bar{border-left:1.5px solid var(--ink);padding-left:6px}

/* ---------- lunch & dinner ---------- */
.lunch{padding-top:10px}
.lunch .menu-title{font-size:20px;margin-bottom:6px}
.dinner-row{display:flex;align-items:flex-start;margin-top:4px}
.dinner-badge{width:59px;height:76px;background:var(--orange);color:var(--white);font-size:9px;font-weight:800;line-height:10.5px;text-align:center;display:flex;align-items:center;justify-content:center;margin-left:-14px;margin-right:6px}

.section-rule{position:absolute;left:0;right:0;top:256px;height:2px;background:var(--slate)}
.combo-title{position:absolute;left:50%;top:240px;transform:translateX(-50%);background:var(--cream);padding:0 16px;font-family:"Lobster",sans-serif;font-size:28px;color:var(--slate);white-space:nowrap}
.combo-title span{color:var(--red)}

.combo-grid{position:absolute;left:31px;top:297px;width:483px;height:370px;border:4px solid var(--red);display:grid;grid-template-columns:repeat(3,1fr);grid-template-rows:repeat(4,1fr)}
.combo{position:relative;overflow:hidden}
.combo--dark{background:var(--ink);color:var(--yellow)}
.combo--light{background:var(--yellow);color:var(--ink)}
.combo__num{position:absolute;left:2px;top:2px;width:42px;height:42px}
.combo__num text{font-family:"Montserrat",sans-serif;font-weight:900;font-size:21px;fill:var(--ink)}
.combo__name{position:absolute;left:50px;top:10px;font-size:11px;font-weight:800;white-space:nowrap}
.combo__day{position:absolute;right:6px;top:23px;font-family:"Lobster",sans-serif;font-size:11.5px}
.combo--dark .combo__day{color:var(--white)}
.combo--light .combo__day{color:var(--red)}
.combo__photo{position:absolute;left:24px;right:10px;bottom:6px;height:52px;border-radius:40% 40% 30% 30%;background:radial-gradient(ellipse at 50% 50%,#e79a3f,#b5561c 60%,rgba(120,50,20,0) 100%)}
</style>
</head>
<body>

<!-- Outside spread -->
<section class="sheet sheet--outside">
  <div class="cover">
    <div class="cover__flank cover__flank--left"></div>
    <div class="cover__center">
      <div class="cover__rot">
        <p class="cover__address">4810 Harbor Street N Bayview, FL 33000</p>
        <p class="cover__phone">555-014-2290</p>
        <p class="cover__tagline">Great food - Made fresh!</p>
        <p class="cover__name">The Crispy Coop</p>
      </div>
    </div>
    <div class="cover__flank cover__flank--right"></div>
  </div>

  <div class="platters">
    <div class="platters__rot">
      <div class="platters__head">
        <p class="platters__title">☆PARTY<br><span>PLATTERS</span>☆</p>
        <p class="platters__sub">For All Occasions</p>
      </div>
      <p class="platters__lead">WE CAN CREATE<br>THE IDEAL CUSTOM PLATTER<br>FOR ANY OCCASION.</p>
      <p class="platters__body">Whether it's game day, birthday, employee celebration or a holiday gathering, our assortments of chicken, ribs, tenders, gizzards, fish, shepherd's pie, and many other items are second to none.</p>
      <div class="platters__photo" role="img" aria-label="Photo of fried chicken wings in a fryer basket with fries and dipping sauces"></div>
      <p class="platters__cta">CALL US TO MAKE YOUR NEXT EVENT<br><b>SPECTACULAR!</b></p>
      <p class="platters__phone">555-014-2290</p>
    </div>
  </div>

  <div class="breakfast">
    <h2 class="menu-title"><span class="star">✪</span><span class="hot">BREAKFAST</span> MENU<span class="star">✪</span><small>(Served Until 10:30)</small></h2>
    <div class="menu-cols">
      <div>
        <h3 class="col-head">Chicken/ Fish</h3>
        <ul class="items">
          <li class="red">CHICKEN LEG</li>
          <li>CHICKEN WING</li>
          <li class="red">CHICKEN THIGH</li>
          <li>CHICKEN BREAST</li>
          <li class="red">CHICKEN TENDERS (1/2LB)</li>
          <li>FISH <span class="script">Friday Only!</span></li>
          <li class="red">8PC DARK</li>
          <li>8PC MIXED</li>
          <li class="red">8PC WHITE</li>
          <li>GIZZARDS/ LIVERS (1/2LB)</li>
        </ul>
      </div>
      <div>
        <h3 class="col-head">Meals</h3>
        <ul class="items">
          <li>BREAKFAST COMBO<span class="note">(Any 3 small side items)</span></li>
          <li class="red">ADD GRAVY</li>
          <li>BISCUIT &amp; GRAVY</li>
          <li class="red">STEAK &amp; GRAVY</li>
          <li>WEDGES &amp; GRAVY</li>
          <li class="red">2pc DARK SNACK<span class="note" style="color:var(--ink)">(Leg and thigh with wedges)</span></li>
          <li>2pc WHITE SNACK<span class="note">(Breast and wing with wedges)</span></li>
          <li class="red">TENDER SNACK<span class="note" style="color:var(--ink)">(1/2LB with wedges)</span></li>
        </ul>
      </div>
      <div>
        <h3 class="col-head">Sides</h3>
        <p class="size-note">Choose Small/Large Size</p>
        <ul class="items">
          <li class="split"><span>GRITS</span><span class="bar red">CORNED BEEF HASH</span></li>
          <li>POTATO WEDGES</li>
          <li class="red">EGGS</li>
        </ul>
        <ul class="boxed">
          <li>BACON/ SAUSAGE (3)</li>
          <li class="red">COUNTRY FRIED STEAK</li>
          <li>HASH BROWNS (2)</li>
          <li class="red">CORN DOG/ EGGROLL</li>
          <li>POPPERS (5)/ POTATO BALL</li>
        </ul>
      </div>
    </div>
  </div>
</section>

<!-- Inside spread -->
<section class="sheet sheet--inside">
  <div class="lunch">
    <h2 class="menu-title"><span class="star">✪</span><span class="hot">LUNCH &amp; DINNER</span> MENU<span class="star">✪</span></h2>
    <div class="menu-cols" style="padding:0 0 0 0;grid-template-columns:172px 172px 186px;column-gap:13px">
      <div>
        <h3 class="col-head">Chicken/ Fish</h3>
        <ul class="items" style="line-height:15.4px">
          <li class="red">CHICKEN LEG</li>
          <li>CHICKEN WING</li>
          <li class="red">CHICKEN THIGH</li>
          <li>CHICKEN BREAST</li>
          <li class="red">CHICKEN TENDERS (1/2LB)</li>
          <li>FISH <span class="script">Friday Only!</span></li>
          <li class="red">8pc DARK</li>
          <li>8pc MIXED</li>
          <li class="red">8pc WHITE</li>
          <li>GIZZARDS/ LIVERS (1/2LB)</li>
        </ul>
      </div>
      <div>
        <h3 class="col-head">Meals</h3>
        <ul class="items" style="padding-left:6px;line-height:13px">
          <li>2pc DARK SNACK<span class="note">(Leg and thigh with wedges)</span></li>
          <li class="red">2pc WHITE SNACK<span class="note" style="color:var(--ink)">(Breast and wing with wedges)</span></li>
          <li>TENDER SNACK<span class="note">(1/2LB with wedges)</span></li>
        </ul>
        <div class="dinner-row">
          <div class="dinner-badge">ALL<br>DINNERS<br>INCLUDE<br>2 SMALL<br>SIDES</div>
          <ul class="items" style="padding-left:0;line-height:13px">
            <li>2pc DARK DINNER</li>
            <li class="red">2pc WHITE DINNER</li>
            <li>TENDER DINNER</li>
            <li class="red">ENTRE'E OF THE DAY</li>
            <li>BBQ RIB DINNER</li>
            <li class="red">FISH DINNER</li>
          </ul>
        </div>
      </div>
      <div>
        <h3 class="col-head">Sides</h3>
        <p class="size-note">Choose Small/Large Size</p>
        <ul class="items" style="line-height:13px">
          <li>POTATO WEDGES</li>
          <li class="red">RICE</li>
          <li>MASHED POTATOES</li>
          <li class="red">VEGETABLE OF THE DAY</li>
          <li>MAC &amp; CHEESE</li>
        </ul>
        <ul class="boxed" style="margin-right:20px;margin-left:0">
          <li>CORN DOG/ EGGROLL</li>
          <li class="red">JALAPENO POPPERS (5)</li>
          <li>POTATO BALL</li>
        </ul>
      </div>
    </div>
  </div>

  <div class="section-rule"></div>
  <h2 class="combo-title"><span>Combo</span> Meals</h2>

  <div class="combo-grid">
    <div class="combo combo--dark"><svg class="combo__num" viewBox="0 0 42 42"><polygon points="21,1 26,15 41,15 29,24 33,40 21,30 9,40 13,24 1,15 16,15" fill="#d8282a"/><text x="21" y="30" text-anchor="middle" style="fill:#fff">1</text></svg><p class="combo__name">DARK SNACK</p><div class="combo__photo" role="img" aria-label="Fried chicken leg and thigh with potato wedges"></div></div>
    <div class="combo combo--light"><svg class="combo__num" viewBox="0 0 42 42"><polygon points="21,1 26,15 41,15 29,24 33,40 21,30 9,40 13,24 1,15 16,15" fill="#1d1d1d"/><text x="21" y="30" text-anchor="middle" style="fill:#fff">2</text></svg><p class="combo__name">WHITE SNACK</p><div class="combo__photo" role="img" aria-label="Fried chicken breast and wing with wedges"></div></div>
    <div class="combo combo--dark"><svg class="combo__num" viewBox="0 0 42 42"><polygon points="21,1 26,15 41,15 29,24 33,40 21,30 9,40 13,24 1,15 16,15" fill="#d8282a"/><text x="21" y="30" text-anchor="middle" style="fill:#fff">3</text></svg><p class="combo__name">4pc MIXED</p><div class="combo__photo" role="img" aria-label="Four pieces of mixed fried chicken"></div></div>

    <div class="combo combo--light"><svg class="combo__num" viewBox="0 0 42 42"><polygon points="21,1 26,15 41,15 29,24 33,40 21,30 9,40 13,24 1,15 16,15" fill="#1d1d1d"/><text x="21" y="30" text-anchor="middle" style="fill:#fff">4</text></svg><p class="combo__name">4pc DARK</p><div class="combo__photo" role="img" aria-label="Four pieces of dark meat fried chicken"></div></div>
    <div class="combo combo--dark"><svg class="combo__num" viewBox="0 0 42 42"><polygon points="21,1 26,15 41,15 29,24 33,40 21,30 9,40 13,24 1,15 16,15" fill="#d8282a"/><text x="21" y="30" text-anchor="middle" style="fill:#fff">5</text></svg><p class="combo__name">2pc DARK MEAL</p><div class="combo__photo" role="img" aria-label="Dark meat chicken meal with mac and cheese and mashed potatoes"></div></div>
    <div class="combo combo--light"><svg class="combo__num" viewBox="0 0 42 42"><polygon points="21,1 26,15 41,15 29,24 33,40 21,30 9,40 13,24 1,15 16,15" fill="#d8282a"/><text x="21" y="30" text-anchor="middle" style="fill:#fff">6</text></svg><p class="combo__name">2pc WHITE MEAL</p><div class="combo__photo" role="img" aria-label="White meat chicken meal with two sides"></div></div>

    <div class="combo combo--light"><svg class="combo__num" viewBox="0 0 42 42"><polygon points="21,1 26,15 41,15 29,24 33,40 21,30 9,40 13,24 1,15 16,15" fill="#d8282a"/><text x="21" y="30" text-anchor="middle" style="fill:#fff">7</text></svg><p class="combo__name">3pc LEG SNACK</p><div class="combo__photo" role="img" aria-label="Three fried chicken legs with wedges"></div></div>
    <div class="combo combo--dark"><svg class="combo__num" viewBox="0 0 42 42"><polygon points="21,1 26,15 41,15 29,24 33,40 21,30 9,40 13,24 1,15 16,15" fill="#fbe820"/><text x="21" y="30" text-anchor="middle">8</text></svg><p class="combo__name">3pc WING SNACK</p><div class="combo__photo" role="img" aria-label="Three fried chicken wings with wedges"></div></div>
    <div class="combo combo--light"><svg class="combo__num" viewBox="0 0 42 42"><polygon points="21,1 26,15 41,15 29,24 33,40 21,30 9,40 13,24 1,15 16,15" fill="#1d1d1d"/><text x="21" y="30" text-anchor="middle" style="fill:#fff">9</text></svg><p class="combo__name">TENDER SNACK</p><div class="combo__photo" role="img" aria-label="Chicken tenders with potato wedges"></div></div>

    <div class="combo combo--light"><svg class="combo__num" viewBox="0 0 42 42"><polygon points="21,1 26,15 41,15 29,24 33,40 21,30 9,40 13,24 1,15 16,15" fill="#1d1d1d"/><text x="21" y="30" text-anchor="middle" style="fill:#fff;font-size:17px">10</text></svg><p class="combo__name">TENDER DINNER</p><div class="combo__photo" role="img" aria-label="Chicken tenders with gravy potatoes and peas and carrots"></div></div>
    <div class="combo combo--dark"><svg class="combo__num" viewBox="0 0 42 42"><polygon points="21,1 26,15 41,15 29,24 33,40 21,30 9,40 13,24 1,15 16,15" fill="#d8282a"/><text x="21" y="30" text-anchor="middle" style="fill:#fff;font-size:17px">11</text></svg><p class="combo__name">RIB DINNER</p><p class="combo__day">Thursday Only!</p><div class="combo__photo" role="img" aria-label="Barbecue ribs with mac and cheese and vegetables"></div></div>
    <div class="combo combo--light"><svg class="combo__num" viewBox="0 0 42 42"><polygon points="21,1 26,15 41,15 29,24 33,40 21,30 9,40 13,24 1,15 16,15" fill="#1d1d1d"/><text x="21" y="30" text-anchor="middle" style="fill:#fff;font-size:17px">12</text></svg><p class="combo__name">FISH DINNER</p><p class="combo__day">Friday Only!</p><div class="combo__photo" role="img" aria-label="Fried fish fillets with vegetables and mac and cheese"></div></div>
  </div>
</section>

</body>
</html>
```